Professional Business Cards for Janitorial Company

We are a Janitorial Company that services Commercial Buildings.

Our Logo is included. It can't look silly or cartoonish. Has to look professional.

Information:
Derek Hollin
Operations Manager
760.413.2987
DHollin@BrightwayServicesPV.com
www.BrightwayServicesPV.com

```html
<!DOCTYPE html>
<html lang="en">
<head>
<meta charset="utf-8">
<title>Brightway Services – Business Card</title>
<link rel="stylesheet" href="https://fonts.googleapis.com/css2?family=Open+Sans:wght@400;600;700&display=swap">
<style>
  :root {
    --brand-blue: #33b5e2;
    --ink: #2a2a2a;
    --paper: #ffffff;
    --stage: #3b3d40;
  }
  * { margin: 0; padding: 0; box-sizing: border-box; }
  html, body { width: 1200px; height: 901px; overflow: hidden; }
  body {
    background: var(--stage);
    font-family: "Open Sans", Arial, sans-serif;
    position: relative;
  }
  .card {
    position: absolute;
    width: 525px;
    height: 300px;
    border-radius: 4px;
    overflow: hidden;
  }
  .card-front { left: 338px; top: 120px; background: var(--paper); }
  .card-back { left: 338px; top: 481px; background: var(--brand-blue); }

  .front-band {
    position: absolute; left: 0; right: 0; top: 262px; height: 22px;
    background: var(--brand-blue);
  }

  .wordmark {
    position: absolute;
    display: flex;
    align-items: center;
    gap: 10px;
    font-weight: 700;
    line-height: 1.05;
  }
  .wordmark-square { width: 34px; height: 34px; flex: none; }
  .wordmark-name { font-size: 22px; }

  .card-front .wordmark { right: 40px; top: 70px; color: var(--brand-blue); }
  .card-front .wordmark-square { border: 4px solid var(--brand-blue); }

  .contact { position: absolute; left: 150px; top: 138px; }
  .contact-name { font-size: 19px; font-weight: 700; color: var(--ink); line-height: 1.3; }
  .contact-title { font-size: 12px; color: var(--brand-blue); margin-bottom: 8px; }
  .contact-row {
    display: flex; align-items: center; gap: 8px;
    font-size: 11.5px; color: var(--ink); height: 18px;
  }
  .contact-row svg { width: 13px; height: 13px; flex: none; }
  .icon-fill { fill: var(--brand-blue); }
  .icon-line { stroke: var(--paper); fill: none; }

  .card-back .wordmark { left: 178px; top: 104px; color: var(--paper); }
  .card-back .wordmark-square { border: 4px solid var(--paper); }
  .card-back .wordmark-name { font-size: 28px; }
  .back-url {
    position: absolute; left: 34px; top: 252px;
    color: var(--paper); font-size: 13px; letter-spacing: 0.2px;
  }
  .back-stripe { position: absolute; right: 0; height: 10px; width: 70px; background: var(--paper); }
  .back-stripe.one { top: 240px; }
  .back-stripe.two { top: 262px; width: 40px; }
</style>
</head>
<body>

  <section class="card card-front" aria-label="Business card front">
    <div class="front-band"></div>

    <div class="wordmark">
      <span class="wordmark-square"></span>
      <span class="wordmark-name">Brightway<br>Services</span>
    </div>

    <div class="contact">
      <p class="contact-name">Derek Hollin</p>
      <p class="contact-title">Operations Manager</p>
      <p class="contact-row">
        <svg viewBox="0 0 16 16" aria-hidden="true"><path class="icon-fill" d="M3 1h3l1.5 4-2 1.2a9 9 0 0 0 4.3 4.3L11 8.5l4 1.5v3a2 2 0 0 1-2 2A12 12 0 0 1 1 3a2 2 0 0 1 2-2z"/></svg>
        760.413.2987
      </p>
      <p class="contact-row">
        <svg viewBox="0 0 16 16" aria-hidden="true"><rect class="icon-fill" x="1" y="3" width="14" height="10"/><path class="icon-line" d="M1 3l7 6 7-6" stroke-width="1.4"/></svg>
        DHollin@BrightwayServicesPV.com
      </p>
      <p class="contact-row">
        <svg viewBox="0 0 16 16" aria-hidden="true"><circle class="icon-fill" cx="8" cy="8" r="7"/><path class="icon-line" d="M1 8h14M8 1c-3 3-3 11 0 14M8 1c3 3 3 11 0 14" stroke-width="1"/></svg>
        www.BrightwayServicesPV.com
      </p>
    </div>
  </section>

  <section class="card card-back" aria-label="Business card back">
    <div class="wordmark">
      <span class="wordmark-square"></span>
      <span class="wordmark-name">Brightway<br>Services</span>
    </div>
    <p class="back-url">www.BrightwayServicesPV.com</p>
    <span class="back-stripe one"></span>
    <span class="back-stripe two"></span>
  </section>

</body>
</html>
```